Medical centre needs a business card

We are a medcial centre in Australia, needing a new business card. Our demographic is low working class families. We are going to be renovating our premises to modernise the look and also had a new logo done a few months ago representing quality and community, and now need to update our cards. It needs to be doubled sided, with logo and contact details on the front, and appointment details on the back. . Needs to be modern and simple, easy to read. <br/><br/>Name: Fern Vale Medical Centre <br/>Address: 512 Kestrel Rd (Cnr Kestrel Rd & Lindon Park Rd),<br/>Corvane Court Shopping Centre, Paralowie, SA 5108<br/>Ph: 08 8361 4027<br/>Tag line: Where every visit counts for you<br/>Website: www.fernvalemedicalcentre.example.au<br/>Online bookings also available<br/><br/>(On the back, to have 3 lines of appointments that can be written in.<br/>Day, date, time)<br/><br/>Your next appointment is on<br/>Can try “M T W Th F Sa Su _________________ at ____________ am/pm” or other combinations <br/>Please advise as soon as possible if unable to attend<br/>Cancellation fees apply if less than 2 hrs notice<br/>Online appointments available (please highlight this option by either by position, colour or font)

Target Market(s)

Lower social economic working class, young families to seniors

Industry/Entity Type

Medical Centre

Contact Information for Business Card

Fern Vale Medical Centre
512 Kestrel Rd (Cnr Kestrel Rd & Lindon Park Drive)
Corvane Court Shopping Centre
Marrowby SA 5190
Ph: 08 8361 4027
www.fernvalemedicalcentre.example.au
Tagline line: where every visit counts for you
Back side is for appointments
Your next appointment is with Dr ______________
Day/date/time (Please give 3 lines of appointments)
Please advise as soon as possible if unable to attend
Cancellation fees apply if less than 2 hours notice
Online appointments available
Book online easily and conveniently (please highlight online appointments)

Font styles to use
Serif
Sans Serif

Colors

Designer to choose colors to be used in the design.

Requirements
Must have
• Modern and simple
• Easy to ready
• Induces a wellbeing feeling
• Incorporate our logo colours and feel from logo
• Induces feeling of stability and security
Nice to have
• Attract attention
• Pleasant to look at
• Feeling of innovation
Should not have
• Loud clashing colours
• Overly luxurious feeling
• Overly artistic

```html
<!DOCTYPE html>
<html lang="en">
<head>
<meta charset="utf-8">
<title>Fern Vale Medical Centre – Business Card</title>
<link rel="stylesheet" href="https://fonts.googleapis.com/css2?family=Oswald:wght@500&family=Roboto:wght@400;500;700&display=swap">
<style>
  :root {
    --blue: #1a86d0;
    --blue-deep: #0f6fb8;
    --blue-light: #2aa3e3;
    --green: #8cc63f;
    --ink: #3a3a3a;
    --white: #ffffff;
    --backdrop: #d9d9d9;
  }
  * { box-sizing: border-box; margin: 0; padding: 0; }
  html, body { width: 1200px; height: 800px; overflow: hidden; }
  body {
    background: var(--backdrop);
    font-family: "Roboto", Arial, sans-serif;
    display: flex; align-items: center; justify-content: center; gap: 40px;
  }
  .card {
    width: 560px; height: 320px; position: relative; overflow: hidden;
    box-shadow: 0 6px 18px rgba(0,0,0,.18);
  }

  /* Front */
  .card-front { background: var(--white); }
  .brand {
    position: absolute; left: 34px; top: 32px;
    display: flex; align-items: center; gap: 10px;
  }
  .brand-mark { width: 22px; height: 22px; background: var(--blue); flex: none; }
  .brand-name {
    font-weight: 700; font-size: 20px;
    color: var(--blue); letter-spacing: .5px; line-height: 1.1;
  }
  .contact {
    position: absolute; left: 34px; top: 98px;
    font-style: normal;
    color: var(--ink); font-size: 12.5px; line-height: 1.45;
  }
  .contact .org { font-weight: 700; }
  .contact-line { display: flex; align-items: center; gap: 7px; margin-top: 3px; }
  .contact-line svg { width: 12px; height: 12px; flex: none; }
  .person { position: absolute; right: 34px; top: 124px; text-align: right; }
  .person-name {
    font-family: "Oswald", sans-serif; font-weight: 500; font-size: 24px;
    color: var(--blue); letter-spacing: .5px; line-height: 1.2;
  }
  .person-role {
    font-family: "Oswald", sans-serif; font-weight: 500; font-size: 16px;
    color: var(--green); letter-spacing: 1px; line-height: 1.3;
  }
  .band-accent {
    position: absolute; left: 0; right: 0; bottom: 44px; height: 5px;
    background: var(--blue-light);
  }
  .tagline-band {
    position: absolute; left: 0; right: 0; bottom: 0; height: 40px;
    background: var(--blue);
    color: var(--white); font-weight: 700; font-size: 14px; letter-spacing: .6px;
    text-transform: uppercase; display: flex; align-items: center; padding-left: 34px;
  }

  /* Back */
  .card-back {
    background: radial-gradient(circle at 55% 45%, var(--blue-light) 0%, var(--blue) 55%, var(--blue-deep) 100%);
    color: var(--white); padding: 26px 34px;
  }
  .appt-title {
    text-align: center; font-size: 19px; font-weight: 500; letter-spacing: 1.5px;
    color: rgba(255,255,255,.85); margin-bottom: 14px;
  }
  .field-row {
    display: flex; align-items: flex-end; gap: 6px;
    font-size: 11.5px; font-weight: 500; letter-spacing: .4px;
    color: rgba(255,255,255,.85); height: 26px;
  }
  .fill { flex: 1; border-bottom: 1px dotted rgba(255,255,255,.7); height: 1px; margin-bottom: 3px; }
  .fill.short { flex: .8; }
  .notice {
    text-align: center; font-size: 11px; line-height: 1.4; margin-top: 18px;
  }
  .book-online {
    text-align: center; font-weight: 700; font-size: 15px; letter-spacing: .4px;
    text-transform: uppercase; margin-top: 8px;
  }
</style>
</head>
<body>

<section class="card card-front" aria-label="Business card front">
  <div class="brand">
    <span class="brand-mark"></span>
    <span class="brand-name">FERN VALE<br>MEDICAL CENTRE</span>
  </div>

  <address class="contact">
    <div class="org">Fern Vale Medical Centre</div>
    <div>512 Kestrel Rd</div>
    <div>(Cnr Kestrel Rd &amp; Lindon Park Drive)</div>
    <div>Corvane Court Shopping Centre</div>
    <div>Marrowby SA 5190</div>
    <div class="contact-line">
      <svg viewBox="0 0 24 24" aria-hidden="true"><path fill="#1a86d0" d="M6.6 10.8a15 15 0 0 0 6.6 6.6l2.2-2.2c.3-.3.7-.4 1-.2 1.1.4 2.3.6 3.6.6.6 0 1 .4 1 1V20c0 .6-.4 1-1 1A17 17 0 0 1 3 4c0-.6.4-1 1-1h3.5c.6 0 1 .4 1 1 0 1.3.2 2.5.6 3.6.1.3 0 .7-.2 1z"/></svg>
      <span>08 8361 4027</span>
    </div>
    <div class="contact-line">
      <svg viewBox="0 0 24 24" aria-hidden="true"><circle cx="12" cy="12" r="10" fill="#1a86d0"/><path d="M2 12h20M12 2c3 3 3 17 0 20M12 2c-3 3-3 17 0 20" stroke="#fff" stroke-width="1.5" fill="none"/></svg>
      <span>fernvalemedicalcentre.example.au</span>
    </div>
  </address>

  <div class="person">
    <div class="person-name">DANIEL HARTLEY</div>
    <div class="person-role">PRESIDENT</div>
  </div>

  <div class="band-accent"></div>
  <div class="tagline-band">Where every visit counts for you</div>
</section>

<section class="card card-back" aria-label="Business card back">
  <h2 class="appt-title">APPOINTMENTS</h2>
  <div class="field-row"><span>YOUR NEXT APPOINTMENT IS WITH DR :</span><span class="fill"></span></div>
  <div class="field-row">
    <span>DAY :</span><span class="fill short"></span>
    <span>DATE :</span><span class="fill short"></span>
    <span>TIME :</span><span class="fill short"></span>
    <span>AM/PM</span>
  </div>
  <div class="field-row"><span class="fill"></span></div>
  <div class="field-row"><span class="fill"></span></div>
  <div class="field-row"><span class="fill"></span></div>
  <p class="notice">Please advise as soon as possible if unable to attend Cancellation fees<br>apply if less than 2 hours notice Online appointments available</p>
  <p class="book-online">Book online easily &amp; conveniently</p>
</section>

</body>
</html>
```